Shopping center investment profile

We need to design a two-page 8.5" x 11" brochure that can be used as a template for profiling our shopping centers and demonstrating our track record to investors.

Our company (KVM Real Estate Investments) owns retail shopping centers in the southwestern United States. Our website is www.kvmtrh.example, but we will be redesigning and modernizing the website and logo in the near future, so please do not use the color schemes or framework of the website for the brochure.

Our investors are institutional and high net worth investors who typically have an existing relationship with our company. They are determining whether to invest multi-millions of dollars in a shopping center opportunity, so the brochure needs to be professional, very high quality and provide key information about the specific property.
Updates

Additional guidance on color scheme:

We would like to see a Blue (something like Hex #5A61BC) and Gold (Hex #EDB215) or (Hex #DDA24B) color scheme with some Black accents 

Thank you!

Target Market(s)

Our target audiences are institutional investors, high net-worth individuals, financial firms and medium to large commercial real estate companies.

Industry/Entity Type

Investment

Requirements
Must have
• Clean and modern look with corresponding fonts and colors.
• Incorporates the information found in the attached "Marlowe Crossing profile" Pages or PDF file.
• Final file design files that can be modified easily
Nice to have
• Two examples of industry brochures are attached. These are examples of the professional quality that we are looking for, not necessarily the design or format.

```html
<!DOCTYPE html>
<html lang="en">
<head>
<meta charset="utf-8">
<title>KVM Real Estate Investments – Investor Presentation</title>
<link href="https://fonts.googleapis.com/css2?family=Roboto+Condensed:wght@400;700&family=Open+Sans:wght@400;600;700&family=Tinos:wght@700&family=Lato:wght@300&display=swap" rel="stylesheet">
<style>
:root{
  --blue:#5a61bc;
  --blue-dark:#454b9e;
  --navy:#2f3477;
  --gold:#edb215;
  --gold-soft:#dda24b;
  --black:#121212;
  --white:#ffffff;
  --ink:#3a3a3a;
  --grey:#8a8a8a;
  --canvas:#ececec;
}
*{box-sizing:border-box;margin:0;padding:0}
html,body{width:1200px;height:1000px;overflow:hidden;background:var(--canvas)}
body{position:relative;font-family:"Open Sans",sans-serif;color:var(--ink)}
.page{position:absolute;top:134px;width:565px;height:731px;background:var(--white);overflow:hidden;box-shadow:0 2px 10px rgba(0,0,0,.18)}
.cover{left:25px}
.profile{left:610px}

/* ---------- cover ---------- */
.cover-edge{position:absolute;left:0;top:0;width:60px;height:100%;background:var(--blue)}
.cover-band{position:absolute;left:60px;top:0;width:100px;height:100%;background:var(--black)}
.cover-column{position:absolute;left:160px;top:0;width:55px;height:300px;background:var(--blue)}
.cover-photo{position:absolute;left:215px;top:0;width:350px;height:300px;
  background:linear-gradient(180deg,#3c4a72 0%,#7780a8 40%,#2c3350 75%,#1d2135 100%)}
.cover-caption{position:absolute;right:24px;top:304px;font-size:11px;color:var(--grey);white-space:nowrap}
.cover-footer{position:absolute;left:160px;bottom:0;width:405px;height:32px;background:var(--blue)}
.cover-gold{position:absolute;left:160px;bottom:32px;width:405px;height:4px;background:var(--gold)}
.cover-right{position:absolute;right:0;top:300px;width:14px;height:431px;background:var(--blue)}
.brand{position:absolute;left:150px;bottom:60px;width:620px;transform-origin:left bottom;transform:rotate(-90deg);white-space:nowrap;color:var(--white);display:flex;align-items:baseline;gap:14px}
.brand-mark{font-family:"Tinos",serif;font-weight:700;font-size:64px;letter-spacing:1px;color:var(--gold)}
.brand-name{font-family:"Lato",sans-serif;font-weight:300;font-size:34px}
.cover-title{position:absolute;left:215px;width:350px;top:505px;text-align:center;color:var(--blue);font-family:"Roboto Condensed",sans-serif;font-weight:700;line-height:1}
.cover-title .line{display:block;font-size:24px}
.cover-title .year{display:block;font-size:28px;color:var(--gold);margin-top:2px}

/* ---------- profile ---------- */
.intro-panel{position:absolute;left:0;top:0;width:218px;height:430px;background:var(--blue);padding:10px 12px 0 18px;color:var(--white)}
.section-title{font-family:"Roboto Condensed",sans-serif;font-weight:700;color:var(--navy);text-align:center}
.intro-panel .section-title{font-size:21px;margin-bottom:6px;color:var(--gold)}
.intro-panel .section-title.results{margin-top:18px}
.bullets{list-style:none}
.bullets li{position:relative;padding-left:10px;font-size:7.6px;line-height:1.35;margin-bottom:5px}
.bullets li::before{content:"•";position:absolute;left:0;top:0;color:var(--gold)}

.profile-header{position:absolute;left:218px;top:8px;width:347px;height:34px;background:var(--blue);color:var(--white);font-family:"Roboto Condensed",sans-serif;font-weight:700;font-size:13px;display:flex;align-items:center;justify-content:center;gap:4px;border-bottom:3px solid var(--gold)}
.profile-header strong{font-size:17px;color:var(--gold)}

.tab{position:absolute;height:14px;padding:0 14px;background:var(--blue);color:var(--white);font-family:"Roboto Condensed",sans-serif;font-weight:700;font-size:7.5px;display:flex;align-items:center;border-radius:7px 7px 0 0;white-space:nowrap}
.photo{position:absolute;top:68px;height:92px}
.photo-before{left:226px;width:168px;background:linear-gradient(180deg,#9fc3e0 0%,#d9e4ea 45%,#b89a78 60%,#8c7a66 100%)}
.photo-after{left:396px;width:162px;background:linear-gradient(180deg,#5f8fc4 0%,#9ab8d8 45%,#a0684e 62%,#5b5f6b 100%)}

.data-table{position:absolute;border-collapse:collapse;font-size:7px}
.data-table td{border:1px solid var(--blue-dark);padding:2px 4px;height:16px;white-space:nowrap}
.data-table .label{background:var(--blue);color:var(--white);font-weight:600}
.data-table .value{text-align:right;color:var(--ink)}
.data-table .note{font-size:5.5px;display:block;font-weight:400}
.data-table .center{text-align:center;font-weight:600;color:var(--navy)}
.data-table .plain{font-weight:600;color:var(--ink)}
.summary{left:224px;top:206px;width:160px}
.invest{left:392px;top:206px;width:168px}
.table-tab{top:193px}

.challenges{position:absolute;left:8px;top:440px;width:206px}
.challenges .section-title{font-size:18px;text-align:left;margin-bottom:8px;color:var(--blue)}
.challenges li{position:relative;padding-left:10px;font-size:8px;line-height:1.35;margin-bottom:6px;color:var(--ink);list-style:none;text-align:justify}
.challenges li::before{content:"•";position:absolute;left:0;color:var(--gold)}
.challenges b{color:var(--navy)}

.tenant{position:absolute;top:418px;height:66px;border:2px solid var(--blue);border-radius:8px;background:var(--white);display:flex;align-items:center;justify-content:center;font-family:"Open Sans",sans-serif;font-weight:600;color:var(--navy);font-size:10px;text-align:center;line-height:1.1}
.tenant-a{left:226px;width:72px}
.tenant-b{left:316px;width:72px}
.tenant-c{left:410px;width:150px;font-size:16px}
.site-map{position:absolute;left:218px;top:500px;width:344px;height:222px;border:4px solid var(--blue);border-radius:22px;background:linear-gradient(160deg,#c9ccd0 0%,#a9adb3 60%,#8f959c 100%)}
.connectors{position:absolute;left:0;top:0}
.page-no{position:absolute;right:6px;bottom:4px;font-size:7px;color:var(--grey)}
</style>
</head>
<body>

<section class="page cover">
  <div class="cover-edge"></div>
  <div class="cover-band"></div>
  <div class="cover-column"></div>
  <div class="cover-photo" role="img" aria-label="Rendering of the renovated shopping center facade under a cloudy sky"></div>
  <div class="cover-caption">Marlowe Crossing</div>
  <div class="cover-right"></div>
  <div class="cover-gold"></div>
  <div class="cover-footer"></div>
  <div class="brand"><span class="brand-mark">KVM</span><span class="brand-name">Real Estate Investments</span></div>
  <h1 class="cover-title"><span class="line">INVESTOR PRESENTATION</span><span class="year">2014</span></h1>
</section>

<section class="page profile">
  <div class="intro-panel">
    <h2 class="section-title">Opportunity</h2>
    <ul class="bullets">
      <li>Bank owned property with attractive purchase price</li>
      <li>Strong relationship with seller's broker and decision makers</li>
      <li>Redevelopment upside with management and leasing</li>
      <li>No major renovations required</li>
      <li>Sagewood location has very strong population, education and income demographics</li>
      <li>Adjacent to premier 2,500-residence master planned community of Cedar Pointe Lakes</li>
      <li>Strong employment area with the new Ridgeview Medical hospital and the adjacent Halvorsen Cancer center</li>
    </ul>
    <h2 class="section-title results">Results</h2>
    <ul class="bullets">
      <li>Stabilized the shopping center within three years, producing excellent results for investors</li>
      <li>Transformed the center into a vibrant destination that the surrounding community is excited about</li>
      <li>Transitioned legacy tenants to upgrade the business operators</li>
      <li>Reduced the shopping center's operating expenses by replacing vendors and appealing property taxes</li>
    </ul>
  </div>

  <header class="profile-header">Marlowe Crossing - <strong>PROPERTY PROFILE</strong></header>

  <div class="tab" style="left:272px;top:54px">BEFORE</div>
  <div class="tab" style="left:448px;top:54px">AFTER</div>
  <div class="photo photo-before" role="img" aria-label="Shopping center before renovation"></div>
  <div class="photo photo-after" role="img" aria-label="Rendering of the shopping center after renovation"></div>

  <div class="tab table-tab" style="left:268px">SUMMARY</div>
  <table class="data-table summary">
    <tr><td class="label">Property Type</td><td class="value">Shopping Center</td></tr>
    <tr><td class="label">Size</td><td class="value">79,490 sq ft</td></tr>
    <tr><td class="label">Purchase</td><td class="value">April 2011</td></tr>
    <tr><td class="label">Total Investment</td><td class="value">$X,XXX,XXX</td></tr>
    <tr><td class="label">Purchase Occupancy</td><td class="value">8.39%</td></tr>
    <tr><td class="label">Total Occupancy</td><td class="value">97.29%</td></tr>
    <tr><td class="label">Projected 5-Year IRR<span class="note">(unleveraged)</span></td><td class="value">XX.XX%</td></tr>
  </table>

  <div class="tab table-tab" style="left:422px">INVESTMENT INFORMATION</div>
  <table class="data-table invest">
    <tr><td class="label">Purchase Price</td><td class="value">$X,XXX,XXX</td></tr>
    <tr><td class="label">Sponsor Acquisition Fee</td><td class="value">$XX,XXX</td></tr>
    <tr><td class="label">Painting &amp; Landscape</td><td class="value">$XXX,XXX</td></tr>
    <tr><td class="label">TI / LC Reserve</td><td class="value">$X,XXX,XXX</td></tr>
    <tr><td colspan="2" class="center">Total Cash Investment</td></tr>
    <tr><td class="label">Investor / Sponsor Split</td><td class="value">XX% / XX%</td></tr>
    <tr><td class="plain">Structure</td><td class="value">Cash Flow Pari Passu</td></tr>
    <tr><td></td><td class="value">Acquisition Fee</td></tr>
    <tr><td></td><td class="value">Management Fee</td></tr>
  </table>

  <div class="challenges">
    <h2 class="section-title">Challenges &amp; Solutions</h2>
    <ul>
      <li><b>Nationwide vacancy rate</b> - KVM did significant due diligence on the property before purchasing the asset, and determined that the location is an A/A-; Tenant improvement and leasing commissions were reserved in order to attract national and regional tenants</li>
      <li><b>Size of Anchor Space</b> - KVM determined that a family-friendly entertainment venue would best serve the demographics in the area instead of another grocer; KVM sought out an experienced operator in Jolly Lanes, who has multiple locations in three states</li>
      <li><b>Curb Appeal</b> - With vacancy and a stigma attached to the center, KVM had to change the center's appeal to the community. KVM worked hand in hand with the Town of Sagewood and the Cedar Pointe Lakes community association to paint the center, upgrade landscaping and add new and larger monument signs</li>
    </ul>
  </div>

  <div class="tenant tenant-a">Jolly<br>Lanes</div>
  <div class="tenant tenant-b">Mesa<br>Cantina</div>
  <div class="tenant tenant-c">Citrine Cafe</div>

  <div class="site-map" role="img" aria-label="Site plan of the center showing parking, pad buildings and tenant locations"></div>
  <svg class="connectors" width="565" height="731" aria-hidden="true">
    <g stroke="var(--gold)" stroke-width="1.4">
      <line x1="262" y1="484" x2="290" y2="640"/>
      <line x1="352" y1="484" x2="455" y2="690"/>
      <line x1="485" y1="484" x2="500" y2="690"/>
    </g>
  </svg>
  <div class="page-no">6</div>
</section>

</body>
</html>
```